Bitcoin Casino User Interface

This is a responsive design for a new bitcoin casino called the brass lantern casino

The 4 games I need the Ui for are video poker, blackjack, roulette and dice

The designs should be ideal for mobile and have a bit of a retro feel

Good example is www.pixelroulettehallcom

Target Market(s)

Adults between the ages of 21-55 all over the world

Industry/Entity Type

Casino

Font styles to use
Serif

Colors
5dc4b5
ffffff

Requirements
Must have
• Must be responsive and look great on mobile
design must be functional
Should not have
• Any generic and standard elements

```html
<!DOCTYPE html>
<html lang="en">
<head>
<meta charset="utf-8">
<title>Brass Lantern Casino App v1 – Roulette</title>
<link rel="stylesheet" href="https://fonts.googleapis.com/css2?family=Inter:wght@400;600;700&family=Zilla+Slab:wght@500;600&family=Libre+Baskerville:ital@1&family=Damion&display=swap">
<style>
:root{
  --teal:#5dc4b5;
  --white:#ffffff;
  --ink:#1c1c1c;
  --black:#1d1d1d;
  --red:#f5423f;
  --blue:#1d8cf0;
  --green:#4fd36b;
  --orange:#f7941d;
  --grey:#7b7b7b;
  --muted:#9a9a9a;
}
*{box-sizing:border-box;margin:0;padding:0}
html,body{width:1200px;height:683px;overflow:hidden;background:var(--white)}
body{position:relative;font-family:"Inter",Helvetica,Arial,sans-serif;color:var(--ink)}
.board-title{position:absolute;left:16px;top:5px;font-size:11px;line-height:13px}
.board-title b{font-weight:700}
.screen-caption{position:absolute;left:273px;top:658px;font-size:15px;font-weight:600}
.app{position:absolute;left:29px;top:198px;width:550px;height:310px;background:var(--teal);box-shadow:0 1px 4px rgba(0,0,0,.35)}
.cell{position:absolute;display:flex;flex-direction:column;align-items:center;justify-content:center;text-align:center}
.stat-label{font-family:"Libre Baskerville",Georgia,serif;font-style:italic;font-size:9px;color:var(--white)}
.stat-value{font-size:9px;font-weight:700;color:var(--white);margin-top:3px}
.credits{left:0;top:0;width:69px;height:45px;background:var(--black)}
.bet{left:69px;top:0;width:69px;height:45px;background:var(--red)}
.result-bar{position:absolute;left:138px;top:0;width:274px;height:45px;background:var(--white)}
.result-bar .stat-label{color:var(--ink);position:absolute}
.result-bar .stat-value{color:var(--ink);position:absolute;font-weight:600;font-size:8.5px}
.verify{position:absolute;left:210px;top:6px;width:59px;height:33px;background:var(--green);color:var(--white);font-family:"Zilla Slab",Georgia,serif;font-size:13px;display:flex;align-items:center;justify-content:center}
.help{left:412px;top:0;width:69px;height:45px;background:var(--blue);color:var(--white);font-family:"Zilla Slab",Georgia,serif;font-size:13px}
.home{left:481px;top:0;width:69px;height:45px;background:var(--black)}
.last-head{left:0;top:45px;width:69px;height:44px;background:var(--grey);font-family:"Libre Baskerville",Georgia,serif;font-style:italic;font-size:9.5px;color:var(--white);line-height:12px}
.last-list{position:absolute;left:0;top:89px;width:69px;height:221px;background:var(--white);list-style:none;padding-top:11px;text-align:center;font-size:8px;line-height:12.8px;letter-spacing:.3px;color:#333}
.auto{left:481px;top:45px;width:69px;height:44px;background:var(--orange);color:var(--white);font-family:"Zilla Slab",Georgia,serif;font-size:13px}
.roll-area{position:absolute;left:481px;top:89px;width:69px;height:133px;background:var(--white)}
.roll-label{position:absolute;left:0;right:0;bottom:7px;text-align:center;font-family:"Libre Baskerville",Georgia,serif;font-style:italic;font-size:9.5px}
.roll-btn{left:481px;width:69px;background:var(--red);color:var(--white);font-family:"Damion",cursive;font-size:21px}
.roll-low{top:222px;height:43px;border-bottom:1px solid #d8312e}
.roll-high{top:265px;height:45px}
.field-label{position:absolute;left:69px;width:412px;text-align:center;font-family:"Zilla Slab",Georgia,serif;font-weight:600;font-size:11px;color:var(--ink)}
.control-row{position:absolute;left:69px;width:412px;height:22px;display:flex}
.control-row .btn{width:69px;height:22px;background:var(--blue);color:var(--white);font-weight:600;font-size:11px;display:flex;align-items:center;justify-content:center}
.control-row .btn.small{font-size:10px}
.input{position:relative;width:137px;height:22px;background:var(--white);display:flex;align-items:center;justify-content:center;font-size:10px;font-weight:600}
.input .unit{position:absolute;right:5px;font-size:9.5px;font-weight:400;color:var(--muted)}
.input.wide-unit .val{margin-left:-6px}
.profit{position:absolute;left:207px;top:222px}
.box{position:absolute;top:265px;height:23px;background:var(--white);display:flex;align-items:center;justify-content:center;font-size:11px;font-weight:600}
.box.placeholder{color:var(--muted);font-weight:400}
</style>
</head>
<body>
<div class="board-title"><b>Brass Lantern Casino App v1:</b> iOS<br>(September 2014)</div>

<main class="app" aria-label="Roulette screen">
  <div class="cell credits"><span class="stat-label">Credits:</span><span class="stat-value">00000</span></div>
  <div class="cell bet"><span class="stat-label">Bet:</span><span class="stat-value">00000</span></div>
  <div class="result-bar">
    <span class="stat-label" style="left:9px;top:10px">Result:</span>
    <span class="stat-value" style="left:9px;top:25px">Lorem Ipsum Dolors Sit Amet</span>
    <span class="stat-label" style="left:144px;top:10px">BTC Payout:</span>
    <span class="stat-value" style="left:146px;top:25px">0000000000</span>
    <span class="verify">Verify</span>
  </div>
  <div class="cell help">Help</div>
  <div class="cell home" aria-label="Home">
    <svg width="18" height="17" viewBox="0 0 18 17" fill="none" stroke="#fff" stroke-width="1.3"><path d="M1.5 8.5 9 1.5l7.5 7M3.5 7v9h4v-5h3v5h4V7"/></svg>
  </div>

  <div class="cell last-head">Last<br>Numbers:</div>
  <ul class="last-list">
    <li>00.0000</li><li>00.0000</li><li>00.0000</li><li>00.0000</li><li>00.0000</li><li>00.0000</li><li>00.0000</li><li>00.0000</li><li>00.0000</li><li>00.0000</li><li>00.0000</li><li>00.0000</li><li>00.0000</li><li>00.0000</li><li>00.0000</li>
  </ul>

  <div class="cell auto">Auto</div>
  <div class="roll-area"><span class="roll-label">Roll:</span></div>
  <div class="cell roll-btn roll-low">Low</div>
  <div class="cell roll-btn roll-high">High</div>

  <div class="field-label" style="top:72px">Payout</div>
  <div class="control-row" style="top:89px">
    <span class="btn">Min</span><span class="btn small">-1</span>
    <span class="input"><span class="val">2</span><span class="unit">X</span></span>
    <span class="btn small">+1</span><span class="btn">Max</span>
  </div>

  <div class="field-label" style="top:116px">Win chance</div>
  <div class="control-row" style="top:133px">
    <span class="btn">Min</span><span class="btn small">-1</span>
    <span class="input"><span class="val" style="font-family:'Zilla Slab',serif;font-size:12px">49.5</span><span class="unit" style="font-size:7px">%</span></span>
    <span class="btn small">+1</span><span class="btn">Max</span>
  </div>

  <div class="field-label" style="top:160px">Bet amount</div>
  <div class="control-row" style="top:177px">
    <span class="btn small">/2</span><span class="btn small">-1</span>
    <span class="input wide-unit"><span class="val">1</span><span class="unit">Credits</span></span>
    <span class="btn small">+1</span><span class="btn small">x2</span>
  </div>

  <div class="field-label" style="top:205px">Profit</div>
  <div class="input wide-unit profit"><span class="val">1</span><span class="unit">Credits</span></div>

  <div class="box placeholder" style="left:138px;width:103px">XX.XXXX</div>
  <div class="box" style="left:264px;width:22px">&gt;</div>
  <div class="box" style="left:309px;width:103px">50.4999</div>
</main>

<div class="screen-caption">Roulette</div>
</body>
</html>
```